Real Estate "For Sale" Sign for construction company

We need a sign that we can use to hang on a post and place on the road when we sell a property. The sign will be simple and will need to mainly feature our logo (files attached), as well as the words "For Sale", and then our phone number "(555) 617 3489". The sign will hang on a post that'll look something like the attached picture.

Target Market(s)

Home buyers

Industry/Entity Type

Real Estate

Font styles to use
Serif
Sans Serif

Colors
0054AA
0677BA
7BADD7
CADEEF
E8F1F8
0094D4
00A9DD
6FCCEA
C7EBF8
E9F6FB

Requirements
Must have
• For Sale & our phone number

```html
<!DOCTYPE html>
<html lang="en">
<head>
<meta charset="utf-8">
<title>For Sale Sign</title>
<link rel="stylesheet" href="https://fonts.googleapis.com/css2?family=Montserrat:wght@500;600;800&display=swap">
<style>
  :root {
    --backdrop: #3a3a3a;
    --paper-top: #ffffff;
    --paper-bottom: #e8f1f8;
    --brand-blue: #0677ba;
    --deep-blue: #0054aa;
    --sky-blue: #0094d4;
    --pale-blue: #7badd7;
    --navy: #0c2763;
    --navy-dark: #0a1f52;
    --accent-cyan: #6fccea;
    --white: #ffffff;
  }
  * { margin: 0; padding: 0; box-sizing: border-box; }
  html, body {
    width: 1200px;
    height: 2216px;
    overflow: hidden;
    background: var(--backdrop);
  }
  .canvas {
    width: 1200px;
    height: 2216px;
    display: flex;
    align-items: center;
    justify-content: center;
  }
  .sign {
    position: relative;
    width: 1000px;
    height: 1342px;
    overflow: hidden;
    font-family: "Montserrat", Arial, sans-serif;
    background: linear-gradient(180deg, var(--paper-top), var(--paper-bottom) 40%);
    box-shadow: 0 20px 50px rgba(0,0,0,0.35);
  }
  .landscape-art {
    position: absolute;
    left: 0;
    top: 530px;
    width: 100%;
    height: 812px;
    background: linear-gradient(180deg,
      #9cc6e8 0%,
      #4aa9e0 8%,
      #1a8fd2 26%,
      var(--deep-blue) 36%,
      var(--navy) 42%,
      var(--navy-dark) 100%);
  }
  .brand {
    position: absolute;
    top: 130px;
    left: 0;
    width: 100%;
    text-align: center;
    color: var(--brand-blue);
    font-weight: 500;
  }
  .brand-mark {
    display: block;
    width: 150px;
    height: 150px;
    margin: 0 auto 22px;
    border-radius: 50%;
    background: var(--brand-blue);
  }
  .brand-name {
    font-size: 92px;
    line-height: 1;
    letter-spacing: -1px;
  }
  .brand-tag {
    margin-top: 16px;
    font-size: 30px;
    letter-spacing: 14px;
    padding-left: 14px;
  }
  .headline {
    position: absolute;
    top: 645px;
    left: 0;
    width: 100%;
    text-align: center;
    color: var(--white);
    font-weight: 800;
    font-size: 160px;
    line-height: 1;
    letter-spacing: 1px;
  }
  .contact {
    position: absolute;
    top: 990px;
    left: 0;
    width: 100%;
    text-align: center;
  }
  .contact-label {
    color: var(--white);
    font-weight: 500;
    font-size: 60px;
    line-height: 1.1;
    letter-spacing: 1px;
  }
  .contact-phone {
    margin-top: 26px;
    color: var(--accent-cyan);
    font-weight: 600;
    font-size: 106px;
    line-height: 1;
  }
</style>
</head>
<body>
  <main class="canvas">
    <section class="sign">
      <div class="landscape-art" role="img" aria-label="Layered blue mountain ridge illustration fading into a navy valley"></div>

      <div class="brand">
        <span class="brand-mark"></span>
        <div class="brand-name">Highland Ridge</div>
        <div class="brand-tag">PROPERTIES</div>
      </div>

      <h1 class="headline">FOR SALE</h1>

      <div class="contact">
        <p class="contact-label">CALL OR TEXT US AT:</p>
        <p class="contact-phone">(555) 617 3489</p>
      </div>
    </section>
  </main>
</body>
</html>
```